Layout for site fence advertising - length approx. 250 cm x 125 cm

The advertising will later be printed on a PVC film and used for events or on sports fields.

Main services :
Your regional contact at
Real estate and business financing
independent insurance advice

```html
<!DOCTYPE html>
<html lang="en">
<head>
<meta charset="utf-8">
<title>Fence Banner – Lindner Finanzberatung</title>
<link href="https://fonts.googleapis.com/css2?family=Poppins:wght@400;500;600;700&display=swap" rel="stylesheet">
<style>
  :root {
    --page-bg: #f2f2f2;
    --paper: #ffffff;
    --brand-blue: #3d5aa8;
    --band-dark: #2c2c30;
    --text-grey: #555559;
    --photo-light: #c9cacc;
    --photo-dark: #8e9093;
    --white: #ffffff;
  }
  * { margin: 0; padding: 0; box-sizing: border-box; }
  ul { list-style: none; }
  html, body {
    width: 996px; height: 1200px; overflow: hidden;
    background: var(--page-bg);
    font-family: "Poppins", sans-serif;
  }
  .banner {
    position: absolute; left: 48px; top: 375px;
    width: 900px; height: 450px;
    background: var(--paper);
    overflow: hidden;
    box-shadow: 0 6px 14px rgba(0,0,0,.22);
  }
  .banner-shapes { position: absolute; inset: 0; }
  .brand {
    position: absolute; left: 131px; top: 50px; white-space: nowrap;
  }
  .brand-name {
    font-size: 15px; font-weight: 600; color: var(--brand-blue); line-height: 1.2;
  }
  .brand-tagline {
    font-size: 12px; font-weight: 500; color: var(--text-grey); margin-top: 2px;
  }
  .headline {
    position: absolute; left: 39px; top: 137px;
    color: var(--white); white-space: nowrap;
  }
  .headline-title {
    font-size: 50px; font-weight: 700; line-height: 46px;
  }
  .headline-sub {
    font-size: 33px; font-weight: 400; line-height: 40px; margin-top: 4px; letter-spacing: .3px;
  }
  .service {
    position: absolute; top: 302px; white-space: nowrap;
    color: var(--white); font-size: 20px; font-weight: 500; line-height: 30px;
    display: flex; align-items: center; gap: 5px;
  }
  .service svg { width: 16px; height: 16px; }
  .contact-label {
    position: absolute; left: 29px; top: 366px; white-space: nowrap;
    font-size: 25px; font-weight: 600; line-height: 27px; color: var(--text-grey);
  }
  .phone-pill {
    position: absolute; left: 250px; top: 359px; width: 329px; height: 39px;
    background: var(--brand-blue); border-radius: 20px; white-space: nowrap;
    display: flex; align-items: center; justify-content: center; gap: 8px;
    color: var(--white); font-size: 30px; font-weight: 600; letter-spacing: .5px;
  }
  .phone-pill svg { width: 24px; height: 24px; }
  .website {
    position: absolute; left: 250px; top: 401px; width: 329px; text-align: center;
    white-space: nowrap; line-height: 32px;
    font-size: 23px; font-weight: 600; color: var(--text-grey); letter-spacing: 1.2px;
  }
  .name-plate {
    position: absolute; left: 607px; top: 379px; width: 300px; height: 36px;
    background: var(--band-dark); border-radius: 18px 0 0 18px; white-space: nowrap;
    color: var(--white); font-size: 26px; font-weight: 500;
    display: flex; align-items: center; padding-left: 19px; letter-spacing: .3px;
  }
</style>
</head>
<body>
<main class="banner">
  <svg class="banner-shapes" viewBox="0 0 900 450" width="900" height="450">
    <defs>
      <linearGradient id="photoTone" x1="0" y1="0" x2="0.4" y2="1">
        <stop offset="0" stop-color="var(--photo-light)"/>
        <stop offset="0.65" stop-color="#b3b5b7"/>
        <stop offset="1" stop-color="var(--photo-dark)"/>
      </linearGradient>
    </defs>
    <circle cx="73" cy="71" r="42" fill="none" stroke="var(--brand-blue)" stroke-width="3"/>
    <line x1="124" y1="27" x2="124" y2="115" stroke="var(--text-grey)" stroke-width="2"/>
    <rect class="band-blue" x="0" y="126" width="900" height="160" fill="var(--brand-blue)"/>
    <rect class="band-dark" x="0" y="286" width="900" height="62" fill="var(--band-dark)"/>
    <line x1="187" y1="294" x2="187" y2="340" stroke="#8a8a8e" stroke-width="1"/>
    <line x1="327" y1="294" x2="327" y2="340" stroke="#8a8a8e" stroke-width="1"/>
    <line x1="445" y1="294" x2="445" y2="340" stroke="#8a8a8e" stroke-width="1"/>
    <circle cx="900" cy="262" r="276" fill="var(--paper)"/>
    <circle cx="900" cy="262" r="272" fill="url(#photoTone)" stroke="var(--brand-blue)" stroke-width="6"
            role="img" aria-label="Portrait photo of the adviser in a dark suit in front of a faded city skyline"/>
    <line x1="600" y1="376" x2="900" y2="376" stroke="var(--band-dark)" stroke-width="1.5"/>
    <line x1="600" y1="418" x2="900" y2="418" stroke="var(--band-dark)" stroke-width="1.5"/>
  </svg>

  <div class="brand">
    <p class="brand-name">Lindner Finanzberatung GmbH</p>
    <p class="brand-tagline">Finanzieren, Versichern, Vorsorgen</p>
  </div>

  <div class="headline">
    <h1 class="headline-title">REAL ESTATE AND<br>BUSINESS FINANCING</h1>
    <p class="headline-sub">Independent Insurance Adviser</p>
  </div>

  <ul class="services">
    <li class="service" style="left:37px"><svg viewBox="0 0 16 16"><path d="M2 9l4 4 8-10" fill="none" stroke="#fff" stroke-width="2"/></svg>Investment</li>
    <li class="service" style="left:196px"><svg viewBox="0 0 16 16"><path d="M2 9l4 4 8-10" fill="none" stroke="#fff" stroke-width="2"/></svg>Financing</li>
    <li class="service" style="left:335px"><svg viewBox="0 0 16 16"><path d="M2 9l4 4 8-10" fill="none" stroke="#fff" stroke-width="2"/></svg>Leasing</li>
    <li class="service" style="left:455px"><svg viewBox="0 0 16 16"><path d="M2 9l4 4 8-10" fill="none" stroke="#fff" stroke-width="2"/></svg>Insurance</li>
  </ul>

  <p class="contact-label">YOUR REGIONAL<br>CONTACT AT</p>

  <p class="phone-pill">
    <svg viewBox="0 0 24 24"><path d="M6.6 3.5l2.6 3.2-1.6 2.2c.9 2.3 2.9 4.4 5.4 5.5l2.1-1.6 3.3 2.6-1.4 3.1C11 18.5 5.4 12.9 3.5 4.9z" fill="none" stroke="#fff" stroke-width="1.8" stroke-linejoin="round"/><path d="M14 3.5a7 7 0 0 1 6.5 6.5M14 7a3.5 3.5 0 0 1 3 3" fill="none" stroke="#fff" stroke-width="1.6"/></svg>
    +43 660 123 4567
  </p>
  <p class="website">www.lindner-finanz.at</p>

  <p class="name-plate">MARKUS LINDNER</p>
</main>
</body>
</html>
```